Stationery and business card design
TradeNimbus
Stationery and business card design -
Creative Brief
Corporate
Marcella Quenby, PHR, PMP
Project Manager
4172 Birchwell Rd NE #20591 Oakhollow, MI 48273
mquenby@tradenimbus.example
http://www.tradenimbus.example
stationary will be for corporate entity no specific individual

```html
<!DOCTYPE html>
<html lang="en">
<head>
<meta charset="utf-8">
<title>TradeNimbus Stationery</title>
<link href="https://fonts.googleapis.com/css2?family=Roboto:wght@400;700&display=swap" rel="stylesheet">
<style>
  :root {
    --brand-blue: #1f4f9e;
    --brand-blue-deep: #173c7a;
    --brand-orange: #f3a21c;
    --paper: #ffffff;
    --paper-shade: #eef1f5;
    --line-grey: #d5dae2;
    --stage: #e7e4df;
    --ink: #2d3a52;
  }
  * { margin: 0; padding: 0; box-sizing: border-box; }
  html, body { width: 1200px; height: 852px; overflow: hidden; }
  body {
    position: relative;
    background: var(--stage);
    font-family: "Roboto", Arial, sans-serif;
    color: var(--ink);
  }
  .piece { position: absolute; background: var(--paper); box-shadow: 0 2px 6px rgba(0,0,0,.18); }
  .wordmark { color: var(--brand-blue); font-weight: 700; letter-spacing: -0.5px; white-space: nowrap; }

  .logo-tile { left: 12px; top: 19px; width: 288px; height: 118px; border-radius: 10px; display: flex; align-items: center; padding-left: 40px; }
  .logo-tile .wordmark { font-size: 38px; }

  .envelope-back { left: 41px; top: 161px; width: 386px; height: 271px; background: none; box-shadow: none; }
  .envelope-back svg { display: block; filter: drop-shadow(0 2px 4px rgba(0,0,0,.18)); }

  .envelope-front { left: 41px; top: 420px; width: 547px; height: 240px; }
  .envelope-front .edge-band { position: absolute; right: 0; top: 0; width: 10px; height: 100%; background: var(--brand-blue); }
  .envelope-front .wordmark { position: absolute; left: 40px; top: 30px; font-size: 32px; }
  .envelope-front .return-address { position: absolute; left: 42px; top: 80px; font-size: 8.5px; line-height: 12px; color: var(--brand-blue); width: 170px; }

  .letterhead { left: 437px; top: 24px; width: 494px; height: 701px; }
  .letterhead .edge-band { position: absolute; right: 0; top: 0; width: 14px; height: 100%; background: var(--brand-blue); }
  .letterhead .wordmark { position: absolute; left: 40px; top: 40px; font-size: 32px; }
  .letterhead .footer { position: absolute; left: 40px; bottom: 24px; font-size: 8.5px; line-height: 13px; color: var(--brand-blue); }
  .letterhead .footer .web { color: var(--brand-orange); }

  .business-card { left: 962px; top: 607px; width: 214px; height: 70px; }
  .business-card .edge-band { position: absolute; right: 0; top: 0; width: 6px; height: 100%; background: var(--brand-blue); }
  .business-card .wordmark { position: absolute; left: 14px; top: 10px; font-size: 14px; }
  .business-card .holder { position: absolute; left: 14px; top: 36px; font-size: 5.5px; line-height: 7.5px; color: var(--brand-orange); }
  .business-card .contact { position: absolute; left: 112px; top: 34px; font-size: 5.5px; line-height: 7px; color: var(--brand-blue); width: 92px; }
</style>
</head>
<body>
  <div class="piece logo-tile"><span class="wordmark">TradeNimbus</span></div>

  <div class="piece envelope-back">
    <svg width="386" height="271" viewBox="0 0 386 271">
      <rect x="0" y="0" width="386" height="271" fill="var(--paper)"/>
      <path d="M0 0 L193 150 L386 0" fill="none" stroke="var(--line-grey)" stroke-width="1"/>
      <path d="M0 271 L150 160 M386 271 L236 160" fill="none" stroke="var(--line-grey)" stroke-width="1"/>
      <path d="M0 150 Q193 210 386 150 L386 200 Q193 265 0 200 Z" fill="var(--brand-blue)"/>
      <path d="M0 200 Q193 265 386 200 L386 208 Q193 275 0 208 Z" fill="var(--brand-blue-deep)"/>
    </svg>
  </div>

  <div class="piece envelope-front">
    <span class="wordmark">TradeNimbus</span>
    <p class="return-address">4172 Birchwell Rd NE #20591<br>Oakhollow, MI 48273</p>
    <div class="edge-band"></div>
  </div>

  <div class="piece letterhead">
    <span class="wordmark">TradeNimbus</span>
    <div class="footer">
      <p>4172 Birchwell Rd NE #20591 Oakhollow, MI 48273</p>
      <p>Tel 616 555 0148 | Fax 616 555 0149 | mquenby@tradenimbus.example</p>
      <p class="web">http://www.tradenimbus.example</p>
    </div>
    <div class="edge-band"></div>
  </div>

  <div class="piece business-card">
    <span class="wordmark">TradeNimbus</span>
    <div class="holder">
      <p>Marcella Quenby, PHR, PMP</p>
      <p>Project Manager</p>
    </div>
    <div class="contact">
      <p>4172 Birchwell Rd NE #20591</p>
      <p>Oakhollow, MI 48273</p>
      <p>T 616 555 0148</p>
      <p>mquenby@tradenimbus.example</p>
    </div>
    <div class="edge-band"></div>
  </div>
</body>
</html>
```